Tri-fold Brochure for Law Firm

Double-sided brochure to be folded into 6 sides tri-fold brochure for an estate planning special for new parents or parents-to-be. Brochure will be placed in classes for new parents/young parents.

Target Market(s)

New Parents Aged 24-34

Industry/Entity Type

Law Firm

Font styles to use
Serif

Requirements
Must have
• The information provided in the word document.
Nice to have
• Highlight the phrase "for New Parents."
• You may use the color scheme from our website:
• http://k47.9dw.sitevaultexample.com/

```html
<!DOCTYPE html>
<html lang="en">
<head>
<meta charset="utf-8">
<title>Harlow Legal – Estate Planning Special for New Parents</title>
<link rel="stylesheet" href="https://fonts.googleapis.com/css2?family=Open+Sans:ital,wght@0,400;0,600;1,600&family=Tinos:wght@400;700&display=swap">
<style>
  :root {
    --backdrop: #e6e2dc;
    --paper: #ffffff;
    --gold: #f2b431;
    --gold-deep: #d9961c;
    --gold-light: #f7cd63;
    --brown: #3b2f24;
    --brown-dark: #241b13;
    --ink: #2b2b2b;
    --pill-text: #f3ece0;
    --portrait-dark: #4a4744;
    --portrait-tone: #7a3b3a;
  }
  * { box-sizing: border-box; margin: 0; padding: 0; }
  html, body { width: 1200px; height: 839px; overflow: hidden; background: var(--backdrop); }
  .brochure {
    position: absolute; left: 30px; top: 24px; width: 1140px; height: 790px;
    background: var(--paper); box-shadow: 0 6px 20px rgba(0,0,0,.18); overflow: hidden;
  }
  .layer { position: absolute; left: 0; top: 0; }
  .fold { position: absolute; top: 0; width: 1px; height: 790px; background: rgba(0,0,0,.08); }
  .fold--one { left: 380px; } .fold--two { left: 760px; }

  .portrait { position: absolute; left: 20px; top: 120px; width: 260px; height: 260px; }
  .portrait__name {
    position: absolute; left: 138px; top: 196px; width: 100px;
    font-family: "Open Sans", sans-serif; font-style: italic; font-weight: 600;
    font-size: 14px; line-height: 1.2; color: #f4f1ec; text-align: right; transform: rotate(-18deg);
  }

  .question {
    position: absolute; left: 34px; top: 405px; width: 318px; height: 42px;
    background: linear-gradient(var(--brown), var(--brown-dark)); border-radius: 8px;
    box-shadow: 0 3px 6px rgba(0,0,0,.3); border: 1px solid #8a7a66;
    font-family: "Tinos", serif; font-weight: 400; font-size: 17px; color: var(--pill-text);
    text-align: center; line-height: 40px; white-space: nowrap; letter-spacing: .3px;
  }
  .intro {
    position: absolute; left: 42px; top: 470px; width: 300px;
    font-family: "Open Sans", sans-serif; font-weight: 600; font-size: 14.5px; line-height: 1.45; color: var(--ink);
  }
  .intro p { margin-bottom: 14px; }

  .firm-mark {
    position: absolute; left: 418px; top: 430px; display: flex; align-items: center; gap: 10px;
    font-family: "Tinos", serif; font-weight: 700; font-size: 19px; color: var(--brown-dark);
  }
  .firm-mark__dot { width: 26px; height: 26px; border-radius: 50%; background: var(--gold); }
  .contact {
    position: absolute; left: 420px; top: 478px; width: 320px; list-style: none;
    font-family: "Open Sans", sans-serif; font-size: 13.5px; line-height: 1.35; color: var(--ink);
  }
  .contact li { display: flex; gap: 8px; margin-bottom: 6px; }
  .contact svg { flex: 0 0 14px; margin-top: 2px; }
  .web-pill {
    position: absolute; left: 430px; top: 610px; width: 270px; height: 36px;
    background: linear-gradient(var(--brown), var(--brown-dark)); border-radius: 8px; border: 1px solid #8a7a66;
    box-shadow: 0 3px 6px rgba(0,0,0,.3);
    font-family: "Open Sans", sans-serif; font-size: 14px; letter-spacing: 2px; color: var(--pill-text);
    text-align: center; line-height: 34px; white-space: nowrap;
  }

  .seal {
    position: absolute; left: 865px; top: 295px; width: 170px; height: 170px; border-radius: 50%;
    background: var(--paper); box-shadow: 0 0 0 3px var(--gold-light), 0 0 0 6px rgba(255,255,255,.7);
    display: flex; align-items: center; justify-content: center;
    font-family: "Tinos", serif; font-weight: 700; font-size: 19px; color: var(--brown-dark); text-align: center;
  }
  .offer {
    position: absolute; left: 770px; top: 500px; width: 360px; text-align: center;
    font-family: "Tinos", serif; color: var(--brown-dark);
  }
  .offer__title { font-size: 16px; font-weight: 700; white-space: nowrap; }
  .offer__title strong { font-size: 19px; }
  .offer__price { font-size: 31px; font-weight: 700; margin: 6px 0 8px; white-space: nowrap; }
  .offer__note { font-size: 16px; font-weight: 700; line-height: 1.25; }
</style>
</head>
<body>
<main class="brochure">
  <svg class="layer" width="1140" height="790" viewBox="0 0 1140 790">
    <defs>
      <linearGradient id="goldFill" x1="0" y1="0" x2="1" y2="1">
        <stop offset="0" stop-color="#f7c34a"/><stop offset="1" stop-color="#eaa826"/>
      </linearGradient>
      <linearGradient id="roomTone" x1="0" y1="0" x2="1" y2="0">
        <stop offset="0" stop-color="#e8eaec"/><stop offset=".5" stop-color="#f3f3f2"/><stop offset="1" stop-color="#e4e6e8"/>
      </linearGradient>
    </defs>
    <path d="M1140,790 H760 C700,560 560,300 380,190 C300,160 200,150 0,158 V120 C200,110 300,120 380,150 C520,200 640,320 760,340 C880,360 1000,300 1140,250 Z" fill="url(#goldFill)"/>
    <path d="M0,140 C200,130 300,140 380,168 C540,230 650,340 760,352 C880,364 1000,316 1140,268" fill="none" stroke="#fff" stroke-opacity=".55" stroke-width="1.5"/>
  </svg>
  <svg class="layer" width="1140" height="360" viewBox="0 0 1140 360" role="img" aria-label="Photo of a smiling young family with a newborn, two children and parents in a bright living room">
    <path d="M0,0 H1140 V250 C1000,300 880,360 760,340 C640,320 520,200 380,150 C300,120 200,110 0,120 Z" fill="url(#roomTone)"/>
  </svg>
  <div class="fold fold--one"></div>
  <div class="fold fold--two"></div>

  <svg class="portrait" width="260" height="260" viewBox="0 0 260 260" role="img" aria-label="Portrait photo of attorney Dana R. Harlow">
    <circle cx="130" cy="130" r="128" fill="#fff" stroke="var(--gold)" stroke-width="3"/>
    <circle cx="130" cy="130" r="118" fill="var(--portrait-dark)" stroke="var(--gold)" stroke-width="3"/>
    <path d="M40,210 C70,190 190,190 220,210 A118,118 0 0 1 40,210 Z" fill="var(--portrait-tone)"/>
  </svg>
  <div class="portrait__name">Dana R.<br>Harlow</div>

  <h2 class="question">Why should every parent have a will?</h2>
  <div class="intro">
    <p>Imagine how many people love your children.</p>
    <p>Would there be a fight over who would care for your children if you passed away without leaving instructions?</p>
    <p>Naming a guardian in your will helps avoid litigation that would cause additional stress to your children and loved ones. You can also name a back-up in the event that your first choice is unable or unwilling to serve as guardian.</p>
  </div>

  <div class="firm-mark"><span class="firm-mark__dot"></span>Harlow Legal, llc</div>
  <ul class="contact">
    <li><svg width="14" height="14" viewBox="0 0 14 14"><path d="M7,1 C4,1 2,3 2,6 C2,9 7,13 7,13 C7,13 12,9 12,6 C12,3 10,1 7,1 Z" fill="var(--gold-deep)"/><circle cx="7" cy="6" r="2" fill="#fff"/></svg><span>47 Elm Court Road,<br>Suite 310, Fairview, MD 21000</span></li>
    <li><svg width="14" height="14" viewBox="0 0 14 14"><rect x="3" y="1" width="8" height="12" rx="1.5" fill="var(--gold-deep)"/><rect x="4.5" y="3" width="5" height="7" fill="#fff"/></svg><span>(410)-555-0142</span></li>
    <li><svg width="14" height="14" viewBox="0 0 14 14"><path d="M3,1 L5,1 L6,4 L4.5,5.5 C5.5,7.5 6.5,8.5 8.5,9.5 L10,8 L13,9 L13,11 C13,12 12,13 11,13 C6,12 2,8 1,3 C1,2 2,1 3,1 Z" fill="var(--gold-deep)"/></svg><span>(410)-555-0187</span></li>
    <li><svg width="14" height="14" viewBox="0 0 14 14"><rect x="1" y="3" width="12" height="8" fill="var(--gold-deep)"/><path d="M1,3 L7,8 L13,3" fill="none" stroke="#fff" stroke-width="1"/></svg><span>dana@harlow-legal.com</span></li>
  </ul>
  <div class="web-pill">www.harlow-legal.com</div>

  <div class="seal">Harlow Legal, llc</div>
  <div class="offer">
    <p class="offer__title">Estate Planning Special for <strong>New Parents</strong></p>
    <p class="offer__price">$750 per couple</p>
    <p class="offer__note">For parents-to-be and parents of children<br>under 5 years old.</p>
  </div>
</main>
</body>
</html>
```